Mirvald Health & Wellness needs a fresh and interesting website

I need a rebrand and redevelopment of my website, www.tessapinlowe.com
Our mission is provide bespoke , lifestyle medicine , everyone has their own path to health. and we are creating a personalized experience for people to life their life to the fullest
Mirvald - means sea lands
I need an landing page and about page and potentially a few project launch pages , I have been using Wordpress for my basic information and then I use Kartra for the launch pages of my programs since I can edit those easily.

Target Market(s)

Corporate and individual's who are interested in a different perspective on health and wellness , and living with a chronic illness

Industry/Entity Type

Health, lifestyle , wellness coaching and medicine

Coding

Number of Pages Required

2 page

Font styles to use
Other font styles liked:
• look into the logo

Requirements
Must have
• the logo I uploaded
Nice to have
• I want a fresh perspective on health, I have bamboo, hibiscus vibes in my logo , but also like more of a water vibe/ I want something earthy but not too boho it needs to be clean
Should not have
• every other holistic health vibe,

```html
<!DOCTYPE html>
<html lang="en">
<head>
<meta charset="utf-8">
<title>Mirvald Health &amp; Wellness</title>
<link href="https://fonts.googleapis.com/css2?family=Frank+Ruhl+Libre:wght@500;600&family=Lato:wght@400;700&family=Crimson+Text&display=swap" rel="stylesheet">
<style>
:root{
  --teal:#1a6577;
  --teal-dark:#17605a;
  --green:#6cab2b;
  --green-light:#7cb832;
  --text:#2f2f2f;
  --muted:#555;
  --cream:#f6f1e3;
  --white:#fff;
  --gold:#e0a526;
}
*{box-sizing:border-box;margin:0;padding:0}
html,body{width:1200px;height:3636px;overflow:hidden;background:var(--white)}
body{position:relative;font-family:"Lato",sans-serif;color:var(--text)}
.abs{position:absolute}
.serif{font-family:"Frank Ruhl Libre",serif;font-weight:500;color:var(--teal)}
.btn{position:absolute;display:flex;align-items:center;justify-content:space-between;height:46px;padding:0 12px 0 20px;border-radius:23px;background:linear-gradient(90deg,var(--teal-dark),var(--green));color:var(--white);font-family:"Frank Ruhl Libre",serif;font-weight:600;font-size:15px;text-decoration:none}
.btn svg{width:22px;height:22px;margin-left:16px}
/* header */
.topbar{top:0;left:0;width:1200px;height:78px}
.topbar .info{position:absolute;top:28px;font-size:14px;color:var(--text);display:flex;align-items:center;gap:10px}
.nav{top:78px;left:0;width:1200px;height:52px;background:linear-gradient(90deg,var(--teal) 0%,#2c7a64 50%,var(--green) 100%)}
.nav a{position:absolute;top:16px;color:var(--white);font-size:16px;text-decoration:none}
.logo-disc{left:463px;top:-40px;width:274px;height:274px;border-radius:50%;background:var(--white);box-shadow:0 6px 18px rgba(0,0,0,.12);text-align:center}
.logo-disc .name{margin-top:130px;font-family:"Frank Ruhl Libre",serif;font-weight:500;color:var(--teal);font-size:46px;line-height:1;letter-spacing:1px}
.logo-disc .tag{font-family:"Frank Ruhl Libre",serif;font-weight:500;color:var(--teal);font-size:12px;letter-spacing:4px;margin-top:4px}
/* hero */
.hero{top:130px;left:0;width:1200px;height:580px}
.hero h1{position:absolute;left:600px;width:530px;top:150px;text-align:center;font-size:60px;line-height:1}
.hero .sub{position:absolute;left:600px;width:530px;top:222px;text-align:center;color:var(--green);font-size:23px}
/* about */
.about h2{left:85px;top:742px;font-size:46px}
.about p{position:absolute;left:85px;width:503px;font-size:15px;line-height:21.5px;text-align:justify;color:var(--text)}
.circle{position:absolute;border-radius:50%}
/* mission */
.eyebrow{color:var(--green);font-size:15px}
.mission h2{left:670px;top:1306px;width:480px;font-size:45px;line-height:53px}
/* events */
.events{top:1640px;left:0;width:1200px;height:700px;background:radial-gradient(ellipse 62% 46% at 50% 50%,#efe7cd 0%,var(--cream) 55%,var(--white) 100%)}
.center{left:0;width:1200px;text-align:center}
/* testimonials */
.card{left:226px;top:2510px;width:746px;height:242px;background:var(--white);box-shadow:0 2px 14px rgba(0,0,0,.12)}
.quote{font-family:"Crimson Text",serif;color:#3d4f58;font-size:18px;line-height:25px;text-align:center}
/* instagram */
.insta{top:2940px;height:250px;width:300px}
/* footer */
.fcol h4{font-family:"Frank Ruhl Libre",serif;font-weight:500;color:var(--teal);font-size:17px;margin-bottom:18px}
.fcol li{list-style:none;font-size:13px;line-height:24px;color:var(--text)}
.divider{position:absolute;top:3368px;width:2px;height:172px;background:#e2e2e2}
.divider::before{content:"";position:absolute;top:0;left:0;width:2px;height:22px;background:var(--green)}
.dots{background:rgba(150,160,165,.08)}
</style>
</head>
<body>

<!-- top bar -->
<header>
  <div class="abs topbar">
    <div class="info" style="left:85px">
      <svg width="16" height="16" viewBox="0 0 24 24"><path d="M12 2a7 7 0 0 0-7 7c0 5 7 13 7 13s7-8 7-13a7 7 0 0 0-7-7zm0 9.5A2.5 2.5 0 1 1 12 6.5a2.5 2.5 0 0 1 0 5z" fill="#6cab2b"/></svg>
      48 W. Alder Lane | Suite 210 | CO 80311
    </div>
    <div class="info" style="left:784px">
      <svg width="16" height="16" viewBox="0 0 24 24"><circle cx="12" cy="12" r="11" fill="#6cab2b"/><path d="M8.5 6.5l2 2.5-1.2 1.5c.8 1.6 2 2.8 3.6 3.6l1.5-1.2 2.5 2-1 2c-4 0-9-5-9-9z" fill="#fff"/></svg>
      (720) 555-0142
    </div>
    <a class="btn" href="#" style="left:945px;top:21px;height:36px;width:170px;font-size:13px;padding:0 7px 0 16px;background:var(--teal)">Book Appointment
      <svg viewBox="0 0 24 24"><circle cx="12" cy="12" r="11" fill="#fff"/><path d="M7 12h9M12.5 8l4 4-4 4" stroke="#1a6577" stroke-width="2" fill="none"/></svg></a>
  </div>
  <nav class="abs nav">
    <a href="#" style="left:85px">Home</a>
    <a href="#" style="left:164px">About Us</a>
    <a href="#" style="left:266px">Our Mission</a>
    <a href="#" style="left:813px">Our Events</a>
    <a href="#" style="left:928px">Testimonials</a>
    <a href="#" style="left:1057px">Contact</a>
  </nav>
  <div class="abs logo-disc">
    <div class="name">MIRVALD</div>
    <div class="tag">HEALTH &amp; WELLNESS</div>
  </div>
</header>

<!-- hero -->
<section class="abs hero">
  <svg class="abs" style="left:0;top:0" width="1200" height="580" viewBox="0 0 1200 580">
    <defs>
      <linearGradient id="heroFill" x1="0" y1="0" x2="1" y2="0">
        <stop offset="0" stop-color="#7b7550"/><stop offset=".45" stop-color="#b9a37a"/><stop offset=".8" stop-color="#f1d9a6"/><stop offset="1" stop-color="#d99a3e"/>
      </linearGradient>
    </defs>
    <g role="img" aria-label="Photo of a smiling couple jogging outdoors at sunrise">
      <rect width="1200" height="580" fill="url(#heroFill)"/>
    </g>
    <path d="M0 460 C120 580 260 580 420 520 C620 440 760 415 900 440 C1040 465 1140 540 1200 580 L0 580Z" fill="#fff"/>
    <path d="M0 430 C80 520 250 590 430 520 C620 445 770 420 920 438 C1050 455 1150 520 1200 570" stroke="#6cab2b" stroke-width="10" fill="none"/>
  </svg>
  <h1 class="serif">Build Your Courage</h1>
  <div class="sub">Discover, Transform, Thrive</div>
  <a class="btn" href="#" style="left:783px;top:274px;width:132px;height:40px;font-size:13px;padding:0 8px 0 17px">Learn More
    <svg viewBox="0 0 24 24"><circle cx="12" cy="12" r="11" fill="#fff"/><path d="M7 12h9M12.5 8l4 4-4 4" stroke="#1a6577" stroke-width="2" fill="none"/></svg></a>
</section>

<!-- about -->
<section class="about">
  <h2 class="abs serif">About Tessa Pinlowe</h2>
  <p style="top:822px">At a young age, I discovered the transformative power of Eastern Medicine when it helped me overcome lung concerns, propelling me toward my dreams as a young athlete. Years later, I faced a pivotal choice: How could I best serve and heal my community? The answer was crystal clear—Eastern Medicine.</p>
  <p style="top:952px">As an Eastern Medicine doctor, I've had the privilege of positively impacting my community through integrative health choices. My journey began after seven years of nurturing creativity and leadership in theatre costume design, when I made the life-altering decision to merge my love for art and science in the field of Acupuncture and Traditional East Asian Medicine (TEAM).</p>
  <a class="btn" href="#" style="left:87px;top:1113px;width:149px">Learn More
    <svg viewBox="0 0 24 24"><circle cx="12" cy="12" r="11" fill="#fff"/><path d="M7 12h9M12.5 8l4 4-4 4" stroke="#1a6577" stroke-width="2" fill="none"/></svg></a>
  <div class="abs dots" style="left:728px;top:660px;width:130px;height:110px;border-radius:50%" role="img" aria-label="Faint dot grid"></div>
  <div class="circle" style="left:702px;top:697px;width:412px;height:412px;background:linear-gradient(160deg,#f4f1dc,#b9c48a 55%,#7f8d52)" role="img" aria-label="Photo of a woman breathing in a sunny meadow"></div>
  <div class="circle" style="left:646px;top:998px;width:182px;height:182px;border:5px solid #fff;background:linear-gradient(150deg,#e9a58a,#c58a6e 60%,#f1ece6)" role="img" aria-label="Portrait of the practitioner"></div>
</section>

<!-- mission -->
<section class="mission">
  <div class="abs dots" style="left:50px;top:1230px;width:322px;height:325px" role="img" aria-label="Faint dot grid"></div>
  <div class="abs" style="left:103px;top:1284px;width:505px;height:338px;border-radius:24px 24px 150px 24px;background:linear-gradient(180deg,#c7cfd0 0%,#a9a994 55%,#5d5740 100%)" role="img" aria-label="Photo of a man meditating on a mountain top"></div>
  <div class="abs eyebrow" style="left:670px;top:1282px">Our Mission</div>
  <h2 class="abs serif">Discover the secrets of a healthy life!</h2>
  <div class="abs" style="left:670px;top:1440px;font-size:18px">Qadipiscing elit, sed do eiusmod tempor.</div>
  <div class="abs" style="left:670px;top:1483px;width:460px;font-size:15px;line-height:21.5px">Adipiscing elit, sed do eiusmod tempor incididunt labore dolore magna aliqua. Ut enim ad minim veniam natus error sit voluptatem accusantium doloremque.</div>
  <a class="btn" href="#" style="left:670px;top:1576px;width:150px">Learn More
    <svg viewBox="0 0 24 24"><circle cx="12" cy="12" r="11" fill="#fff"/><path d="M7 12h9M12.5 8l4 4-4 4" stroke="#1a6577" stroke-width="2" fill="none"/></svg></a>
</section>

<!-- events -->
<section class="abs events">
  <div class="abs" style="left:0;top:120px;width:350px;height:390px;border-radius:40% 60% 50% 30%;background:rgba(214,186,120,.22)" role="img" aria-label="Line illustration of a hibiscus flower"></div>
  <div class="abs" style="left:900px;top:130px;width:280px;height:420px;border-radius:40%;background:rgba(214,186,120,.22)" role="img" aria-label="Line illustration of bamboo stalks"></div>
  <div class="abs center eyebrow" style="top:191px">Our Events</div>
  <h2 class="abs center serif" style="top:232px;font-size:52px">Fall Into YourSelf</h2>
  <p class="abs" style="left:335px;top:312px;width:530px;text-align:center;font-size:15px;line-height:21.5px">Join us for a delightful retreat experience right in the heart of the city, as we come together to honor this season of harvest and letting go, a time to turn inward to expand.</p>
  <div class="abs center" style="top:393px;font-size:20px">Sunday November 5th from 11am-3:15pm</div>
  <a class="btn" href="#" style="left:530px;top:447px;width:150px">Register Now
    <svg viewBox="0 0 24 24"><circle cx="12" cy="12" r="11" fill="#fff"/><path d="M7 12h9M12.5 8l4 4-4 4" stroke="#1a6577" stroke-width="2" fill="none"/></svg></a>
</section>

<!-- testimonials -->
<section>
  <h2 class="abs center serif" style="top:2346px;font-size:52px">Testimonials</h2>
  <div class="abs" style="left:575px;top:2422px;width:50px;height:2px;background:var(--green)"></div>
  <div class="abs dots" style="left:203px;top:2484px;width:196px;height:170px" role="img" aria-label="Faint dot grid"></div>
  <div class="abs dots" style="left:800px;top:2610px;width:200px;height:170px" role="img" aria-label="Faint dot grid"></div>
  <div class="abs card"></div>
  <div class="circle" style="left:558px;top:2464px;width:84px;height:84px;border:3px solid #fff;background:linear-gradient(160deg,#9ed3e0,#c88d6c)" role="img" aria-label="Portrait of the reviewer"></div>
  <p class="abs quote" style="left:280px;top:2569px;width:640px">Lorem Ipsum is simply dummy text of the printing and typesetting industry. Lorem Ipsum has been the industry's standard dummy text ever since the 1500s, when an unknown printer took a galley of type and scrambled it to make</p>
  <div class="abs center" style="top:2656px;font-family:'Crimson Text',serif;color:var(--teal);font-size:27px;letter-spacing:1px">DANIEL R.</div>
  <div class="abs center" style="top:2708px;color:var(--gold);font-size:20px;letter-spacing:1px">★★★★★</div>
  <svg class="abs" style="left:574px;top:2785px" width="54" height="12"><circle cx="7" cy="6" r="4" fill="#1a6577"/><circle cx="27" cy="6" r="3.5" fill="none" stroke="#1a6577"/><circle cx="47" cy="6" r="3.5" fill="none" stroke="#1a6577"/></svg>
</section>

<!-- instagram -->
<section>
  <h2 class="abs center serif" style="top:2850px;font-size:52px">Follow us on Instagram</h2>
  <div class="abs insta" style="left:0;background:linear-gradient(160deg,#e8c1ae,#c99683)" role="img" aria-label="Photo of a woman meditating in a plant-filled room"></div>
  <div class="abs insta" style="left:300px;background:linear-gradient(180deg,#b8c3c9,#4d5358 70%,#1e1f20)" role="img" aria-label="Silhouettes of two people doing yoga at dusk"></div>
  <div class="abs insta" style="left:600px;background:linear-gradient(160deg,#d9d9d9,#6a6a6a)" role="img" aria-label="Black and white portrait of a woman in a hat"></div>
  <div class="abs insta" style="left:900px;background:linear-gradient(160deg,#b8d08c,#c99a88 60%,#7a8c5e)" role="img" aria-label="Photo of a group stretching outdoors"></div>
  <svg class="abs" style="left:14px;top:3052px" width="18" height="26"><path d="M14 3L4 13l10 10" stroke="#fff" stroke-width="2.5" fill="none"/></svg>
  <svg class="abs" style="left:1168px;top:3052px" width="18" height="26"><path d="M4 3l10 10L4 23" stroke="#fff" stroke-width="2.5" fill="none"/></svg>
  <a class="abs" href="#" style="left:473px;top:3228px;width:254px;height:59px;display:flex;align-items:center;justify-content:center;gap:12px;background:linear-gradient(90deg,var(--teal-dark),var(--green));color:#fff;font-size:15px;font-weight:700;text-decoration:none">
    <span style="width:18px;height:18px;border:2px solid #fff;border-radius:3px"></span>FOLLOW US @MIRVALD</a>
</section>

<!-- footer -->
<footer>
  <div class="abs" style="left:70px;top:3440px;width:290px;text-align:center">
    <div style="font-family:'Frank Ruhl Libre',serif;font-weight:500;color:var(--teal);font-size:52px;line-height:1;letter-spacing:1px">MIRVALD</div>
    <div style="font-family:'Frank Ruhl Libre',serif;font-weight:500;color:var(--teal);font-size:13px;letter-spacing:4px;margin-top:4px">HEALTH &amp; WELLNESS</div>
  </div>
  <div class="divider" style="left:403px"></div>
  <div class="divider" style="left:693px"></div>
  <div class="divider" style="left:901px"></div>
  <div class="abs fcol" style="left:439px;top:3364px">
    <h4>CONTACT US</h4>
    <ul>
      <li style="line-height:18px">48 W. Alder Lane<br>Suite 210 Denver, CO 80311</li>
      <li style="margin-top:14px">Phone:&nbsp; (720) 555-0178</li>
      <li style="margin-top:14px">info@mirvald.com</li>
    </ul>
  </div>
  <div class="abs fcol" style="left:744px;top:3364px">
    <h4>MAIN MENU</h4>
    <ul><li>&gt; Home</li><li>&gt; About Us</li><li>&gt; Our Mission</li><li>&gt; Our Events</li><li>&gt; Testimonials</li><li>&gt; Contact</li></ul>
  </div>
  <div class="abs fcol" style="left:956px;top:3364px">
    <h4>USEFUL LINKS</h4>
    <ul><li>&gt; Facebook</li><li>&gt; Twitter</li><li>&gt; Linkedin</li><li>&gt; Instagram</li><li>&gt; Youtube</li></ul>
  </div>
  <div class="abs" style="left:0;top:3583px;width:1200px;height:1px;background:#dcdcdc"></div>
  <div class="abs center" style="top:3600px;font-size:15px">Copyright © 2024 Mirvald Health &amp; Wellness&nbsp; |&nbsp; All Right Reserved</div>
</footer>

</body>
</html>
```